Rocket business card

Modern business card design, use of color is good with clean space too.

Things to include on card:

Quote: I add fuel to your optometry practice

- Eyewear Sales
- Admin Duties
- Revenue Collection
- Leadership
- Tech Adoption
- COGS Reduction
- Product Sourcing
-Medical Growth

Dalton Vessey, CEO
Glint Harbor
Text Me! 847-302-1964
dalton@glintharbor.example

```html
<!DOCTYPE html>
<html lang="en">
<head>
<meta charset="utf-8">
<title>Glint Harbor business card</title>
<link rel="stylesheet" href="https://fonts.googleapis.com/css2?family=Roboto+Condensed:wght@300;400;700&display=swap">
<style>
  :root {
    --backdrop: #d9dbde;
    --ink: #0a0a0a;
    --paper: #ffffff;
    --orange: #f07a22;
    --amber: #f7a21b;
    --text-light: #f2f2f2;
  }
  * { box-sizing: border-box; margin: 0; padding: 0; }
  html, body {
    width: 1200px; height: 800px; overflow: hidden;
    background: var(--backdrop);
    font-family: "Roboto Condensed", Arial, sans-serif;
  }
  .stage {
    width: 1200px; height: 800px;
    display: flex; align-items: center; justify-content: center; gap: 80px;
  }
  .card {
    position: relative;
    width: 360px; height: 630px;
    background: var(--ink);
    overflow: hidden;
    box-shadow: 0 10px 28px rgba(0,0,0,0.25);
  }

  /* Front */
  .front-split { position: absolute; inset: 0; }
  .brand {
    position: absolute; top: 78px; left: 0; right: 0;
    display: flex; align-items: center; justify-content: center; gap: 14px;
  }
  .brand-dot {
    width: 26px; height: 26px; border-radius: 50%;
    background: var(--orange);
  }
  .brand-name {
    font-weight: 300; font-size: 40px; letter-spacing: 5px;
    color: var(--ink); text-transform: uppercase;
  }
  .identity {
    position: absolute; top: 360px; left: 0; right: 0; text-align: center;
  }
  .person-name {
    font-weight: 700; font-size: 30px; letter-spacing: 0.5px;
    color: var(--orange); text-transform: uppercase;
  }
  .person-role {
    font-weight: 400; font-size: 20px; color: var(--text-light); margin-top: 2px;
  }
  .contact-icons {
    display: flex; justify-content: center; gap: 8px; margin-top: 30px;
  }
  .contact-icons svg { width: 16px; height: 16px; }
  .contact-list {
    list-style: none; margin-top: 12px;
    font-weight: 400; font-size: 20px; line-height: 28px; color: var(--text-light);
  }

  /* Back */
  .tagline {
    position: absolute; top: 70px; left: 0; right: 0; text-align: center;
    font-weight: 400; font-size: 21px; line-height: 25px; color: var(--text-light);
    text-transform: uppercase;
  }
  .tagline .fuel { color: var(--amber); }
  .services {
    position: absolute; top: 200px; left: 0; right: 0; text-align: center;
    list-style: none;
    font-weight: 300; font-size: 20px; line-height: 32px; color: var(--text-light);
  }
</style>
</head>
<body>
<main class="stage">

  <section class="card card-front" aria-label="Card front">
    <svg class="front-split" viewBox="0 0 360 630" preserveAspectRatio="none" aria-hidden="true">
      <path d="M0 0 H360 V240 C300 250 250 200 180 215 C110 230 60 300 0 310 Z" fill="var(--paper)"/>
    </svg>
    <div class="brand">
      <span class="brand-dot"></span>
      <span class="brand-name">Glint Harbor</span>
    </div>
    <div class="identity">
      <h1 class="person-name">Dalton Vessey</h1>
      <p class="person-role">CEO</p>
      <div class="contact-icons">
        <svg viewBox="0 0 16 16" aria-label="Phone"><path d="M4 2 L6.5 2 L7.5 5 L6 6.2 C6.8 8 8 9.2 9.8 10 L11 8.5 L14 9.5 L14 12 C14 13 13 14 12 14 C7 14 2 9 2 4 C2 3 3 2 4 2 Z" fill="var(--orange)"/></svg>
        <svg viewBox="0 0 16 16" aria-label="Email"><rect x="1.5" y="3.5" width="13" height="9" fill="none" stroke="var(--orange)" stroke-width="1.5"/><path d="M1.5 3.5 L8 9 L14.5 3.5" fill="none" stroke="var(--orange)" stroke-width="1.5"/></svg>
        <svg viewBox="0 0 16 16" aria-label="Website"><circle cx="8" cy="8" r="6.3" fill="none" stroke="var(--orange)" stroke-width="1.4"/><ellipse cx="8" cy="8" rx="2.8" ry="6.3" fill="none" stroke="var(--orange)" stroke-width="1.2"/><path d="M1.7 8 H14.3" stroke="var(--orange)" stroke-width="1.2"/></svg>
      </div>
      <ul class="contact-list">
        <li>847-302-1964</li>
        <li>dalton@glintharbor.example</li>
        <li>www.glintharbor.example</li>
      </ul>
    </div>
  </section>

  <section class="card card-back" aria-label="Card back">
    <p class="tagline">I add <span class="fuel">fuel</span><br>to your<br>optometry practice</p>
    <ul class="services">
      <li>Eyewear Sales</li>
      <li>Admin Duties</li>
      <li>Revenue Collection</li>
      <li>Leadership</li>
      <li>Tech Adoption</li>
      <li>COGS Reduction</li>
      <li>Product Sourcing</li>
      <li>Medical Growth</li>
    </ul>
  </section>

</main>
</body>
</html>
```